Quillory Nest Business Card

I need a business card design. We are a collaborate online training company. Our colors are gray and green. Our website is QuilloryNest.com

I would like an area for a profile picture within the card

```html
<!DOCTYPE html>
<html lang="en">
<head>
<meta charset="utf-8">
<title>Quillory Nest Business Card</title>
<link rel="stylesheet" href="https://fonts.googleapis.com/css2?family=Arimo:wght@400;700&display=swap">
<style>
  :root {
    --page: #2a2622;
    --card-top: #3a4044;
    --card-bottom: #24282b;
    --green: #7cc63a;
    --text: #f2f4f3;
  }
  * { margin: 0; padding: 0; box-sizing: border-box; }
  html, body { width: 1200px; height: 800px; overflow: hidden; }
  body {
    background: var(--page);
    font-family: "Arimo", Arial, sans-serif;
    color: var(--text);
    display: flex;
    align-items: center;
    justify-content: center;
    gap: 40px;
  }
  .card {
    position: relative;
    width: 540px;
    height: 309px;
    background: linear-gradient(160deg, var(--card-top), var(--card-bottom));
    border-radius: 3px;
    box-shadow: 0 12px 30px rgba(0,0,0,.45);
    overflow: hidden;
  }
  /* Front */
  .card-front .top-rule {
    position: absolute; left: 0; right: 0; top: 66px;
    height: 2px; background: var(--green);
  }
  .brand {
    position: absolute; right: 26px; top: 26px;
    display: flex; align-items: center; gap: 8px;
  }
  .brand-dot { width: 16px; height: 16px; border-radius: 50%; background: var(--green); }
  .brand-name { font-weight: 700; font-size: 20px; color: var(--green); letter-spacing: -.3px; }
  .profile-photo {
    position: absolute; left: 62px; top: 96px;
    width: 116px; height: 116px; border-radius: 50%;
    border: 2px solid var(--green);
    background: radial-gradient(circle at 40% 35%, #4d5458, #363b3e);
  }
  .person {
    position: absolute; left: 40px; top: 232px;
  }
  .person-name { font-weight: 700; font-size: 24px; letter-spacing: .5px; }
  .person-title { font-size: 12.5px; color: var(--green); letter-spacing: .3px; margin-top: 2px; }
  .divider {
    position: absolute; left: 262px; top: 110px;
    width: 2px; height: 115px; background: var(--green);
  }
  .contacts {
    position: absolute; left: 286px; top: 92px;
    list-style: none; font-size: 14px; line-height: 24px;
  }
  .contacts li { display: flex; align-items: flex-start; gap: 10px; }
  .contacts svg { flex: none; width: 12px; height: 12px; margin-top: 6px; }
  .contacts .address-line { padding-left: 22px; }
  /* Back */
  .card-back .band-rule {
    position: absolute; left: 0; right: 0; height: 2px; background: var(--green);
  }
  .card-back .band-rule.upper { top: 92px; }
  .card-back .band-rule.lower { top: 206px; }
  .back-brand {
    position: absolute; left: 0; right: 0; top: 126px;
    text-align: center; font-weight: 700; font-size: 42px;
    color: var(--green); letter-spacing: -.8px;
  }
  .back-url {
    position: absolute; left: 0; right: 0; top: 240px;
    text-align: center; font-size: 15px; letter-spacing: 1.5px;
  }
</style>
</head>
<body>
  <section class="card card-front" aria-label="Business card front">
    <div class="brand">
      <span class="brand-dot"></span>
      <span class="brand-name">Quillory Nest</span>
    </div>
    <div class="top-rule"></div>
    <div class="profile-photo" role="img" aria-label="Profile photo area"></div>
    <div class="person">
      <div class="person-name">R ELLISON</div>
      <div class="person-title">ADMINISTRATIVE OFFICER</div>
    </div>
    <div class="divider"></div>
    <ul class="contacts">
      <li>
        <svg viewBox="0 0 12 12" aria-hidden="true"><path d="M2.5 1l2 2.2-1 1.3a6 6 0 0 0 4 4l1.3-1 2.2 2-1.3 1.5C5.5 11 1 6.5 1 2.3z" fill="var(--green)"/></svg>
        <span>(302) 555-0147</span>
      </li>
      <li>
        <svg viewBox="0 0 12 12" aria-hidden="true"><rect x=".5" y="2.5" width="11" height="7.5" fill="var(--green)"/><path d="M.5 2.5l5.5 4 5.5-4" fill="none" stroke="#2b3033" stroke-width="1"/></svg>
        <span>info@quillorynest.com</span>
      </li>
      <li>
        <svg viewBox="0 0 12 12" aria-hidden="true"><g fill="none" stroke="var(--green)" stroke-width="1"><circle cx="6" cy="6" r="5"/><ellipse cx="6" cy="6" rx="2.2" ry="5"/><path d="M1 6h10"/></g></svg>
        <span>www.quillorynest.com</span>
      </li>
      <li>
        <svg viewBox="0 0 12 12" aria-hidden="true"><path d="M6 11.5S2 7 2 4.5a4 4 0 0 1 8 0C10 7 6 11.5 6 11.5z" fill="var(--green)"/><circle cx="6" cy="4.5" r="1.4" fill="#2b3033"/></svg>
        <span>48 Larkmoor Ave. Suite 7</span>
      </li>
      <li class="address-line">Fenwick, Arizona 85000</li>
    </ul>
  </section>

  <section class="card card-back" aria-label="Business card back">
    <div class="band-rule upper"></div>
    <div class="back-brand">Quillory Nest</div>
    <div class="band-rule lower"></div>
    <div class="back-url">www.quillorynest.com</div>
  </section>
</body>
</html>
```